need 4 creative A frame (SANDWICH BOARD) designs concepts for dental office

need 4 creative A frame (SANDWICH BOARD) designs concepts
1 - targeting kids
2. targeting old age
3. targeting teens
4 targeting general public

website - www.brenvaxdental.ca

LINK for Measurements for sandwich board https://www.korvepa.ca/BL_1921/Aluminum-Snap-Edge-A-Frame-Sign

i am attaching certain key ingredients ( rough sketch in uploaded files ) to be added on each design though not mandatory if the design is very creative

```html
<!DOCTYPE html>
<html lang="en">
<head>
<meta charset="utf-8">
<title>Brenvax Dental – A-Frame Board</title>
<link href="https://fonts.googleapis.com/css2?family=Montserrat:wght@500;600;700;800&display=swap" rel="stylesheet">
<style>
  :root {
    --page-bg: #f6f2e6;
    --board-top: #f4f8fb;
    --board-bottom: #cfe6f1;
    --wave: #cde5f0;
    --link-line: #3aa6d6;
    --badge-light: #2bb0e0;
    --badge-dark: #0a7db4;
    --halo: rgba(255, 255, 255, 0.55);
    --ink: #2b2c2e;
    --brand: #6d7075;
    --white: #ffffff;
    --skin-light: #f1e4dc;
    --skin-mid: #e2bfa9;
  }
  * { margin: 0; padding: 0; box-sizing: border-box; }
  html, body {
    width: 1200px;
    height: 1200px;
    overflow: hidden;
    background: var(--page-bg);
    font-family: "Montserrat", sans-serif;
  }
  .board {
    position: absolute;
    left: 180px;
    top: 40px;
    width: 840px;
    height: 1120px;
    overflow: hidden;
    background: linear-gradient(180deg, var(--board-top) 0%, #e6f1f7 45%, var(--board-bottom) 100%);
  }
  .board-art {
    position: absolute;
    inset: 0;
    width: 840px;
    height: 1120px;
  }
  .brand-name {
    position: absolute;
    left: 40px;
    top: 262px;
    font-size: 62px;
    font-weight: 600;
    color: var(--brand);
    letter-spacing: -0.5px;
    white-space: nowrap;
  }
  .badge-text {
    position: absolute;
    color: var(--white);
    font-weight: 700;
    text-align: center;
    line-height: 1;
  }
  .badge-open {
    left: 70px;
    top: 478px;
    width: 222px;
  }
  .badge-open .small { display: block; font-size: 34px; font-weight: 600; }
  .badge-open .big { display: block; font-size: 86px; font-weight: 800; margin: 2px 0 0; }
  .badge-bill {
    left: 607px;
    top: 857px;
    width: 200px;
    font-size: 36px;
    line-height: 1.05;
  }
  .headline {
    position: absolute;
    left: 268px;
    top: 640px;
    font-size: 84px;
    font-weight: 800;
    color: var(--ink);
    letter-spacing: 1px;
    white-space: nowrap;
  }
  .tagline {
    position: absolute;
    left: 270px;
    top: 742px;
    font-size: 36px;
    font-weight: 600;
    color: var(--ink);
    white-space: nowrap;
  }
  .phone {
    position: absolute;
    left: 270px;
    top: 792px;
    font-size: 44px;
    font-weight: 700;
    color: var(--ink);
    letter-spacing: 1px;
    white-space: nowrap;
  }
</style>
</head>
<body>
  <main class="board">
    <svg class="board-art" viewBox="0 0 840 1120" xmlns="http://www.w3.org/2000/svg">
      <defs>
        <linearGradient id="badgeFill" x1="0" y1="0" x2="0" y2="1">
          <stop offset="0" stop-color="var(--badge-light)"/>
          <stop offset="1" stop-color="var(--badge-dark)"/>
        </linearGradient>
        <linearGradient id="photoFill" x1="0" y1="0" x2="1" y2="0">
          <stop offset="0" stop-color="var(--board-top)"/>
          <stop offset="0.35" stop-color="var(--skin-light)"/>
          <stop offset="1" stop-color="var(--skin-mid)"/>
        </linearGradient>
      </defs>

      <rect class="hero-photo" x="339" y="0" width="501" height="560" fill="url(#photoFill)"
            role="img" aria-label="Close-up photo of a smiling mouth with white teeth"/>

      <path class="wave-band" fill="var(--wave)"
            d="M0,505 C140,475 250,452 350,458 C470,466 560,525 660,538 C740,546 800,536 840,528 L840,1120 L0,1120 Z"/>

      <g class="link-lines" stroke="var(--link-line)" stroke-width="2.5" fill="none">
        <line x1="0" y1="520" x2="181" y2="554"/>
        <line x1="181" y1="554" x2="106" y2="814"/>
        <line x1="106" y1="814" x2="345" y2="990"/>
        <line x1="345" y1="990" x2="707" y2="912"/>
        <line x1="707" y1="912" x2="840" y2="982"/>
      </g>

      <g class="badge badge-open-days">
        <circle cx="181" cy="554" r="126" fill="var(--halo)"/>
        <circle cx="181" cy="554" r="111" fill="url(#badgeFill)" stroke="var(--white)" stroke-width="4"/>
      </g>
      <g class="badge badge-tooth">
        <circle cx="106" cy="814" r="76" fill="var(--halo)"/>
        <circle cx="106" cy="814" r="64" fill="url(#badgeFill)" stroke="var(--white)" stroke-width="4"/>
        <path fill="var(--white)"
              d="M92,790 C84,790 80,798 82,808 C84,818 88,826 90,840 C91,846 96,846 97,840 L101,824 C102,820 110,820 111,824 L115,840 C116,846 121,846 122,840 C124,826 128,818 130,808 C132,798 128,790 120,790 C114,790 110,794 106,794 C102,794 98,790 92,790 Z"/>
      </g>
      <g class="badge badge-records">
        <circle cx="345" cy="990" r="88" fill="var(--halo)"/>
        <circle cx="345" cy="990" r="75" fill="url(#badgeFill)" stroke="var(--white)" stroke-width="4"/>
        <rect x="318" y="954" width="54" height="70" rx="4" fill="none" stroke="var(--white)" stroke-width="4"/>
        <rect x="333" y="947" width="24" height="12" rx="3" fill="var(--white)"/>
        <path d="M345,966 v18 M336,975 h18" stroke="var(--white)" stroke-width="5"/>
        <path d="M327,994 h36 M327,1003 h36 M327,1012 h36" stroke="var(--white)" stroke-width="3"/>
      </g>
      <g class="badge badge-direct-bill">
        <circle cx="707" cy="912" r="114" fill="var(--halo)"/>
        <circle cx="707" cy="912" r="100" fill="url(#badgeFill)" stroke="var(--white)" stroke-width="4"/>
      </g>

      <g class="chevrons" fill="var(--badge-dark)">
        <polygon points="455,543 418,575 455,607"/>
        <polygon points="512,543 475,575 512,607"/>
      </g>
    </svg>

    <div class="brand-name">Brenvax Dental</div>

    <div class="badge-text badge-open">
      <span class="small">open</span>
      <span class="big">7</span>
      <span class="small">days</span>
    </div>
    <div class="badge-text badge-bill">we<br>direct<br>bill</div>

    <h1 class="headline">WE’RE IN</h1>
    <p class="tagline">Accepting new patients</p>
    <p class="phone">587 555 0142</p>
  </main>
</body>
</html>
```